Beach Flag for International Watersport Brand

We are a company called Tidefin which develops and sell a new watersport product with the same name.
We need a beach flag design to be used at boatshows and events, but also by dealers and tidefin rentals for promotion and to attract attention. We are thinking of a relatively big beach flag, but the shape depends on what looks good with the design.
The Tidefin is an underwater wing which is towed behind a boat were the user can control the wing to dive down under water to do acrobatics or watch the marine life.

Learn more about the tidefin at our website: www.tidefin-example.com

Access our filevault press folder containing a variety of pictures and material that could be used in designing the beach flag here: https://www.filevault-example.net/sh/k8qz2m5rw1p7tnx/BBKLm4R_2PPd7QWxFcTHNRyDa?dl=0

Industry/Entity Type

Sporting Good

Requirements
Must have
• Tidefin logo
Nice to have
• It would be nice to have some text saying anything of the below:
• "fly under water"
• "experience the sensation of underwater flight"

```html
<!DOCTYPE html>
<html lang="en">
<head>
<meta charset="utf-8">
<title>Tidefin Beach Flag – Fly Under Water</title>
<link rel="stylesheet" href="https://fonts.googleapis.com/css2?family=Exo+2:ital,wght@0,800;1,900&display=swap">
<style>
  :root {
    --backdrop: #f1f2f2;
    --sleeve: #e6e8ea;
    --sleeve-edge: #d3d7da;
    --deep-sea: #0a3f5f;
    --mid-sea: #176f96;
    --shallow-sea: #3f9fbd;
    --light-ray: #bfe6ee;
    --logo-band: #000000;
    --ink-white: #ffffff;
  }
  html, body {
    margin: 0;
    padding: 0;
    width: 1200px;
    height: 2866px;
    overflow: hidden;
    background: var(--backdrop);
  }
  .canvas {
    position: relative;
    width: 1200px;
    height: 2866px;
  }
  .beach-flag {
    position: absolute;
    left: 303px;
    top: 74px;
    width: 594px;
    height: 2718px;
    display: block;
  }
  .flag-sleeve { fill: var(--sleeve); stroke: var(--sleeve-edge); stroke-width: 2; }
  .headline-main {
    font-family: "Exo 2", "Arial Black", sans-serif;
    font-style: italic;
    font-weight: 900;
    font-size: 270px;
    fill: var(--ink-white);
  }
  .headline-sub {
    font-family: "Exo 2", Arial, sans-serif;
    font-weight: 800;
    font-size: 82px;
    fill: var(--ink-white);
  }
  .logo-band { fill: var(--logo-band); }
  .brand-name {
    font-family: "Exo 2", Arial, sans-serif;
    font-weight: 800;
    font-size: 44px;
    letter-spacing: 12px;
    fill: var(--ink-white);
  }
</style>
</head>
<body>
<main class="canvas">
  <svg class="beach-flag" viewBox="0 0 594 2718" xmlns="http://www.w3.org/2000/svg" aria-labelledby="flag-title">
    <title id="flag-title">Tidefin feather beach flag: Fly under water</title>
    <defs>
      <linearGradient id="sea-depth" x1="0" y1="0" x2="0" y2="1">
        <stop offset="0" stop-color="var(--deep-sea)"/>
        <stop offset="0.35" stop-color="var(--mid-sea)"/>
        <stop offset="0.62" stop-color="var(--shallow-sea)"/>
        <stop offset="0.85" stop-color="var(--mid-sea)"/>
        <stop offset="1" stop-color="var(--deep-sea)"/>
      </linearGradient>
      <radialGradient id="sun-glow" cx="130" cy="1950" r="620" gradientUnits="userSpaceOnUse">
        <stop offset="0" stop-color="var(--light-ray)" stop-opacity="0.9"/>
        <stop offset="0.5" stop-color="var(--light-ray)" stop-opacity="0.3"/>
        <stop offset="1" stop-color="var(--light-ray)" stop-opacity="0"/>
      </radialGradient>
      <clipPath id="print-area">
        <path d="M54,2718 L54,690 C54,300 290,22 594,22 L594,2718 Z"/>
      </clipPath>
    </defs>

    <path class="flag-sleeve" d="M1,2717 L1,666 C1,250 250,1 593,1 L593,2717 Z"/>

    <g clip-path="url(#print-area)">
      <g class="underwater-photo" role="img" aria-label="Underwater photo: a rider in fins holding a tidefin wing, silhouetted against sunlit water full of bubbles">
        <rect x="0" y="0" width="594" height="2466" fill="url(#sea-depth)"/>
        <rect x="0" y="0" width="594" height="2466" fill="url(#sun-glow)"/>
      </g>

      <text class="headline-main" transform="translate(376 1170) rotate(-90)" textLength="800" lengthAdjust="spacingAndGlyphs">FLY</text>
      <text class="headline-sub" transform="translate(486 1199) rotate(-90)" textLength="695" lengthAdjust="spacingAndGlyphs">UNDER WATER</text>

      <rect class="logo-band" x="0" y="2466" width="594" height="252"/>
      <text class="brand-name" x="324" y="2608" text-anchor="middle">TIDEFIN</text>
    </g>
  </svg>
</main>
</body>
</html>
```